Business Card Design for Kidvale (Hires out childrens play areas)

Looking to have a business card designed for a company we just bought. The company rents out childrens play areas.

I have uploaded a couple of examples of the kind of business card style I like. Here are two more examples:

https://quorvastudio.nz/project/bright-romp-branding/
https://imgvaultcdn.com/design_img/8841052/302917/302917_5518203_8841052_b73e19a2_image.jpg

I think a white card will be best due to all the colours in the logo.

Size we require: 3.75" x 2.25" (horizontally orientated) with a 0.125" bleed

Uploaded is two versions of our logo.

Details for the card:
1. My name: Liam Verster
2. Title: Managing Director
3. Phone no: 021 563 417
4. Email: liam@kidvale.co.nz
5. URL: www.kidvale.co.nz
6. Address:
PO Box 318625
Fernlea, Auckland

Let me know if you need anything else.

Target Market(s)

Hospitals, doctors surgeries, bed shops, etc.

Contact Information for Business Card

Details for the card:
1. My name: Liam Verster
3. Phone no: 021 563 417
5. URL: www.kidvale.co.nz
6. Address:
PO Box 318625
Fernlea, Auckland

Requirements
Should not have
• Not too busy.

```html
<!DOCTYPE html>
<html lang="en">
<head>
<meta charset="utf-8">
<title>Kidvale Business Card</title>
<link rel="stylesheet" href="https://fonts.googleapis.com/css2?family=Source+Sans+3:wght@400;600;700&display=swap">
<style>
  :root {
    --backdrop-light: #e4e4e4;
    --backdrop-dark: #9a9a9a;
    --card: #ffffff;
    --ink: #1f1f1f;
    --muted: #4a4a4a;
    --brand-blue: #1a5aa6;
    --icon-blue: #2f6fb8;
    --splash-yellow: #f5f7a2;
  }
  * { box-sizing: border-box; margin: 0; padding: 0; }
  html, body {
    width: 1200px;
    height: 1199px;
    overflow: hidden;
  }
  body {
    position: relative;
    background: radial-gradient(ellipse at 50% 45%, var(--backdrop-light) 0%, #c4c4c4 55%, var(--backdrop-dark) 100%);
    font-family: "Source Sans 3", "Helvetica Neue", Arial, sans-serif;
    color: var(--ink);
  }
  .stage-frame {
    position: absolute;
    inset: 3px;
    border: 2px solid #b5b5b5;
  }
  .card {
    position: absolute;
    left: 241px;
    width: 718px;
    height: 431px;
    background: var(--card);
    box-shadow: 0 0 8px rgba(0,0,0,0.45);
  }
  .card--front { top: 104px; }
  .card--back { top: 600px; }

  .brand-mark {
    position: absolute;
    left: 102px;
    top: 134px;
    display: flex;
    align-items: center;
    gap: 8px;
    font-size: 36px;
    font-weight: 700;
    color: var(--brand-blue);
    line-height: 1;
  }
  .brand-mark__dot {
    width: 18px;
    height: 18px;
    border-radius: 50%;
    background: var(--brand-blue);
  }
  .identity {
    position: absolute;
    left: 60px;
    width: 280px;
    top: 228px;
    text-align: center;
  }
  .identity__name {
    font-size: 33px;
    font-weight: 700;
    color: var(--brand-blue);
    line-height: 1.1;
  }
  .identity__title {
    margin-top: 4px;
    font-size: 20px;
    font-weight: 400;
    color: var(--muted);
  }
  .contact {
    position: absolute;
    right: 36px;
    top: 122px;
    text-align: right;
    font-size: 25px;
    line-height: 32px;
    color: var(--ink);
  }
  .contact__line {
    display: flex;
    justify-content: flex-end;
    align-items: center;
    gap: 7px;
  }
  .contact__icon {
    width: 15px;
    height: 15px;
    flex: none;
  }
  .contact__address { margin-top: 18px; }

  .splash {
    position: absolute;
    left: 156px;
    top: 32px;
    width: 430px;
    height: 372px;
  }
  .brand-lockup {
    position: absolute;
    left: 0;
    right: 0;
    top: 172px;
    display: flex;
    justify-content: center;
    align-items: center;
    gap: 12px;
    font-size: 72px;
    font-weight: 700;
    color: var(--brand-blue);
    line-height: 1;
  }
  .brand-lockup__dot {
    width: 30px;
    height: 30px;
    border-radius: 50%;
    background: var(--brand-blue);
  }
</style>
</head>
<body>
  <div class="stage-frame"></div>

  <section class="card card--front">
    <div class="brand-mark"><span class="brand-mark__dot"></span>Kidvale</div>

    <div class="identity">
      <p class="identity__name">Liam Verster</p>
      <p class="identity__title">Managing Director</p>
    </div>

    <div class="contact">
      <p class="contact__line">
        <svg class="contact__icon" viewBox="0 0 16 16" aria-hidden="true">
          <path d="M4 1.5l2.5 3-1.5 1.8c.9 1.9 2.4 3.4 4.3 4.3L11 9l3 2.5-1.3 2.6c-5.6-.5-10.3-5.2-10.8-10.8z" fill="none" stroke="var(--icon-blue)" stroke-width="1.4" stroke-linejoin="round"/>
        </svg>
        021 563 417
      </p>
      <p class="contact__line">
        <svg class="contact__icon" viewBox="0 0 16 16" aria-hidden="true">
          <rect x="1.5" y="3.5" width="13" height="9" fill="none" stroke="var(--icon-blue)" stroke-width="1.3"/>
          <path d="M1.5 3.5L8 9l6.5-5.5" fill="none" stroke="var(--icon-blue)" stroke-width="1.3"/>
        </svg>
        liam@kidvale.co.nz
      </p>
      <p class="contact__line">
        <svg class="contact__icon" viewBox="0 0 16 16" aria-hidden="true">
          <circle cx="8" cy="8" r="6.3" fill="none" stroke="var(--icon-blue)" stroke-width="1.3"/>
          <ellipse cx="8" cy="8" rx="2.7" ry="6.3" fill="none" stroke="var(--icon-blue)" stroke-width="1.1"/>
          <path d="M1.7 8h12.6" stroke="var(--icon-blue)" stroke-width="1.1"/>
        </svg>
        www.kidvale.co.nz
      </p>
      <div class="contact__address">
        <p>PO Box 318625</p>
        <p>Fernlea, Auckland</p>
      </div>
    </div>
  </section>

  <section class="card card--back">
    <svg class="splash" viewBox="0 0 430 372" role="img" aria-label="Soft yellow brush-stroke splash behind the brand name">
      <path d="M120 12 C190 -4 300 8 360 40 C410 70 430 140 422 200 C414 270 380 340 300 362 C220 380 120 370 60 330 C10 295 -4 230 4 170 C12 100 50 30 120 12 Z" fill="var(--splash-yellow)"/>
    </svg>
    <div class="brand-lockup"><span class="brand-lockup__dot"></span>Kidvale</div>
  </section>
</body>
</html>
```